high end contractor

high end contracting company we do all phases of construction kitchen,bathrooms,etc... please look at my website before you design www.harborlinebld.com

would love some sort of lines or logo or both

Industry/Entity Type

Construction

Contact Information for Business Card

company name: harbor & lantern contracting address: 412 birchwood ave Fairhaven NY 10599 email: harborlinebld@mailzone.com website: www.harborlinebld.com office#: 914-555-0182 fax#: 914-555-0197 dominic fersalo mobile# 917-555-0263

```html
<!DOCTYPE html>
<html lang="en">
<head>
<meta charset="utf-8">
<title>Harbor &amp; Lantern Contracting – Business Card</title>
<link rel="stylesheet" href="https://fonts.googleapis.com/css2?family=Open+Sans:wght@300;400&display=swap">
<style>
  :root {
    --backdrop: #d6d6d4;
    --card: #1d1b1c;
    --band: #141314;
    --map-light: #4a4849;
    --map-dark: #2a2829;
    --accent: #3fe0d6;
    --heading: #f2f2f2;
    --body-text: #a3a3a3;
  }
  * { margin: 0; padding: 0; box-sizing: border-box; }
  html, body {
    width: 1200px; height: 702px; overflow: hidden;
    background: var(--backdrop);
    font-family: "Open Sans", Arial, sans-serif;
  }
  .canvas {
    position: relative; width: 1200px; height: 702px;
    display: flex; align-items: center; justify-content: center; gap: 50px;
  }
  .card {
    position: relative; width: 525px; height: 300px;
    background: var(--card); overflow: hidden;
    box-shadow: 0 6px 18px rgba(0,0,0,.25);
  }

  /* Front */
  .street-map {
    position: absolute; inset: 0;
    background: radial-gradient(ellipse at 40% 45%, var(--map-light), var(--map-dark) 75%);
    opacity: .75;
  }
  .name-band {
    position: absolute; left: 0; right: 0; top: 118px; height: 58px;
    background: var(--band);
    display: flex; align-items: center;
    padding-left: 36px;
  }
  .name-band .wordmark {
    display: inline-block;
    font-weight: 300; font-size: 21px; letter-spacing: .5px;
    color: var(--accent); text-transform: uppercase; line-height: 1;
    padding-bottom: 6px;
    border-bottom: 2px solid var(--accent);
  }

  /* Back */
  .company {
    position: absolute; left: 34px; top: 28px;
  }
  .company .title {
    font-weight: 400; font-size: 20px; color: var(--heading); line-height: 1;
  }
  .rule-accent { height: 2px; background: var(--accent); margin-top: 6px; }
  .company .rule-accent { width: 230px; }
  .contact-list {
    list-style: none; margin-top: 6px;
    font-weight: 300; font-size: 15px; line-height: 19px; color: var(--body-text);
  }
  .person {
    position: absolute; right: 34px; bottom: 30px; width: 230px;
  }
  .person .name {
    font-weight: 400; font-size: 18px; color: var(--heading); line-height: 1;
  }
  .person .mobile {
    margin-top: 6px; font-weight: 300; font-size: 15px; color: var(--body-text);
  }
</style>
</head>
<body>
<main class="canvas">
  <section class="card card-front">
    <div class="street-map" role="img" aria-label="Grey street map line pattern covering the card"></div>
    <div class="name-band">
      <span class="wordmark">Harbor &amp; Lantern Renovations</span>
    </div>
  </section>

  <section class="card card-back">
    <div class="company">
      <div class="title">Harbor &amp; Lantern</div>
      <div class="rule-accent"></div>
      <ul class="contact-list">
        <li>412 Birchwood Avenue</li>
        <li>Fairhaven NY 10599</li>
        <li>P: 914-555-0182</li>
        <li>F: 914-555-0197</li>
        <li>harborlinebld@mailzone.com</li>
        <li>www.harborlinebld.com</li>
      </ul>
    </div>
    <div class="person">
      <div class="name">Dominic Fersalo</div>
      <div class="rule-accent"></div>
      <div class="mobile">P: 917-555-0263</div>
    </div>
  </section>
</main>
</body>
</html>
```